Clovane Infographic 2016

I would like to receive an infographic with 2016 company highlights

Attached you'll find the 2015 infographic and new features for the 2016 version

Target Market(s)

relations and new customers

Industry/Entity Type

It Company

Colors
f37122
aaaaaa
ffffff
000000

Requirements
Must have
• look and feel: authority but not arrogant

```html
<!DOCTYPE html>
<html lang="en">
<head>
<meta charset="utf-8">
<title>Clovane Infographic 2016</title>
<link href="https://fonts.googleapis.com/css2?family=Exo+2:wght@300;400;500&display=swap" rel="stylesheet">
<style>
  :root {
    --orange: #f37122;
    --grey: #aaaaaa;
    --dark: #4a4a4a;
    --white: #ffffff;
    --panel-left: #e6e6e6;
    --panel-right: #d9d9d9;
    --faint: #f2f2f2;
    --partner-blue: #2a8fd4;
    --partner-sky: #4fb3e8;
  }
  html, body {
    margin: 0;
    padding: 0;
    width: 1200px;
    height: 1180px;
    overflow: hidden;
    background: var(--white);
  }
  .infographic {
    display: block;
    width: 1200px;
    height: 1180px;
    font-family: "Exo 2", sans-serif;
  }
  .label { font-size: 26px; font-weight: 400; }
  .label-sub { font-size: 26px; font-weight: 300; }
  .stat { font-weight: 400; text-anchor: middle; dominant-baseline: central; }
  .stat-big { font-size: 42px; }
  .stat-mid { font-size: 25px; }
  .stat-wide { font-size: 22px; }
  .stat-small { font-size: 20px; }
  .tag { font-size: 13px; }
  .year { font-size: 54px; font-weight: 400; text-anchor: middle; }
  .fill-orange { fill: var(--orange); }
  .fill-grey { fill: var(--grey); }
  .fill-dark { fill: var(--dark); }
  .fill-white { fill: var(--white); }
  .fill-faint { fill: var(--faint); }
  .right { text-anchor: end; }
  .sponsor { font-size: 30px; font-weight: 400; }
  .brand-name { font-size: 44px; font-weight: 400; }
  .brand-tagline { font-size: 17px; font-weight: 400; }
  .partner { font-size: 25px; font-weight: 500; }
  .chain { fill: none; stroke-width: 8; }
</style>
</head>
<body>
<svg class="infographic" viewBox="0 0 1150 1131" xmlns="http://www.w3.org/2000/svg">
  <defs>
    <radialGradient id="floor-shadow" cx="50%" cy="50%" r="50%">
      <stop offset="0%" stop-color="#9a9a9a" stop-opacity="0.55"/>
      <stop offset="100%" stop-color="#ffffff" stop-opacity="0"/>
    </radialGradient>
  </defs>

  <g class="panels">
    <polygon points="0,14 570,72 570,908 0,908" fill="var(--panel-left)"/>
    <polygon points="580,72 1150,14 1150,908 580,908" fill="var(--panel-right)"/>
  </g>

  <g class="year-banner">
    <polygon points="155,8 995,8 660,46 575,62 490,46" class="fill-orange"/>
    <text x="575" y="52" class="year fill-white">2016</text>
  </g>

  <g class="column-left">
    <path class="chain" stroke="var(--grey)" d="M290,174 L382,228"/>
    <path class="chain" stroke="var(--orange)" d="M382,228 L350,320"/>
    <path class="chain" stroke="var(--dark)" d="M350,320 L420,385"/>
    <path class="chain" stroke="var(--orange)" d="M420,385 L396,478"/>
    <path class="chain" stroke="var(--dark)" d="M396,478 L460,560"/>
    <path class="chain" stroke="var(--grey)" d="M460,560 L375,612"/>
    <path class="chain" stroke="var(--orange)" d="M375,612 L355,710"/>
    <path class="chain" stroke="var(--dark)" d="M355,710 L428,776"/>
    <path class="chain" stroke="var(--orange)" d="M428,776 L357,847"/>
    <path class="chain" stroke="var(--dark)" d="M357,847 L357,908"/>

    <rect x="0" y="160" width="260" height="30" class="fill-grey"/>
    <text x="6" y="184" class="label fill-white">Epic Shit Stickers</text>
    <circle cx="353" cy="128" r="42" class="fill-white"/>
    <circle cx="353" cy="128" r="26" fill="var(--orange)" role="img" aria-label="Sticker icon"/>
    <circle cx="290" cy="174" r="38" fill="var(--white)" stroke="var(--grey)" stroke-width="8"/>
    <text x="290" y="174" class="stat stat-mid fill-grey">1000</text>

    <rect x="0" y="228" width="345" height="30" class="fill-orange"/>
    <text x="6" y="252" class="label fill-white">Employees</text>
    <text x="6" y="281" class="label-sub fill-faint">Growth by 5 people</text>
    <circle cx="450" cy="215" r="40" class="fill-orange"/>
    <circle cx="450" cy="201" r="12" class="fill-white"/>
    <path d="M432,240 L432,228 Q432,216 450,216 Q468,216 468,228 L468,240 Z" class="fill-white"/>
    <circle cx="382" cy="228" r="40" fill="var(--white)" stroke="var(--orange)" stroke-width="8"/>
    <text x="382" y="228" class="stat stat-big fill-orange">18</text>

    <rect x="0" y="303" width="320" height="30" class="fill-white"/>
    <text x="6" y="327" class="label fill-orange">CodeVault Contributions</text>
    <circle cx="408" cy="300" r="28" class="fill-white"/>
    <circle cx="408" cy="300" r="16" fill="var(--dark)" role="img" aria-label="Code repository icon"/>
    <circle cx="350" cy="320" r="38" fill="var(--dark)" stroke="var(--white)" stroke-width="6"/>
    <text x="350" y="320" class="stat stat-mid fill-white">1483</text>

    <rect x="0" y="390" width="390" height="30" class="fill-white"/>
    <text x="6" y="414" class="label fill-orange">Magazines</text>
    <circle cx="475" cy="380" r="38" class="fill-white"/>
    <rect x="466" y="361" width="34" height="40" rx="2" fill="none" stroke="var(--orange)" stroke-width="4"/>
    <line x1="472" y1="372" x2="494" y2="372" stroke="var(--orange)" stroke-width="3"/>
    <line x1="472" y1="382" x2="494" y2="382" stroke="var(--orange)" stroke-width="3"/>
    <line x1="472" y1="392" x2="486" y2="392" stroke="var(--orange)" stroke-width="3"/>
    <circle cx="420" cy="385" r="38" fill="var(--orange)" stroke="var(--white)" stroke-width="6"/>
    <text x="420" y="385" class="stat stat-mid fill-white">6000</text>

    <rect x="0" y="468" width="360" height="30" class="fill-dark"/>
    <text x="6" y="492" class="label fill-white">Certifications</text>
    <circle cx="457" cy="460" r="32" class="fill-dark"/>
    <polygon points="457,443 462,455 475,455 465,463 469,476 457,468 445,476 449,463 439,455 452,455" class="fill-white"/>
    <circle cx="396" cy="478" r="40" fill="var(--white)" stroke="var(--dark)" stroke-width="8"/>
    <text x="396" y="478" class="stat stat-big fill-orange">15</text>

    <rect x="0" y="528" width="430" height="30" class="fill-white"/>
    <text x="6" y="552" class="label fill-orange">MVPS / Regional Directors</text>
    <circle cx="522" cy="530" r="32" class="fill-white"/>
    <circle cx="522" cy="530" r="20" fill="var(--grey)" role="img" aria-label="Award badge"/>
    <circle cx="460" cy="560" r="38" fill="var(--grey)" stroke="var(--white)" stroke-width="6"/>
    <text x="460" y="560" class="stat stat-big fill-white">8</text>

    <rect x="0" y="593" width="340" height="30" class="fill-orange"/>
    <text x="6" y="617" class="label fill-white">Knowledge Expansion</text>
    <circle cx="433" cy="628" r="30" class="fill-orange"/>
    <g stroke="var(--white)" stroke-width="3" fill="none">
      <path d="M421,616 L445,640 M445,616 L421,640"/>
      <path d="M421,624 L421,616 L429,616 M437,616 L445,616 L445,624 M445,632 L445,640 L437,640 M429,640 L421,640 L421,632"/>
    </g>
    <circle cx="375" cy="612" r="40" fill="var(--white)" stroke="var(--orange)" stroke-width="8"/>
    <text x="375" y="597" class="stat stat-small fill-dark">1665</text>
    <text x="375" y="627" class="stat stat-small fill-dark">Hours</text>

    <rect x="0" y="694" width="320" height="30" class="fill-white"/>
    <text x="6" y="718" class="label fill-orange">Sharing Knowledge</text>
    <circle cx="420" cy="697" r="30" class="fill-white"/>
    <circle cx="410" cy="685" r="9" class="fill-dark"/>
    <circle cx="430" cy="709" r="9" class="fill-dark"/>
    <path d="M424,683 A12,12 0 0 1 434,697 M416,711 A12,12 0 0 1 406,697" stroke="var(--orange)" stroke-width="3" fill="none"/>
    <circle cx="355" cy="710" r="40" fill="var(--dark)" stroke="var(--white)" stroke-width="6"/>
    <text x="355" y="695" class="stat stat-small fill-white">1230</text>
    <text x="355" y="725" class="stat stat-small fill-white">Hours</text>

    <rect x="0" y="763" width="400" height="30" class="fill-white"/>
    <text x="6" y="787" class="label fill-orange">Babies Born</text>
    <circle cx="492" cy="782" r="32" class="fill-white"/>
    <circle cx="492" cy="782" r="22" fill="#f7b48a" role="img" aria-label="Baby illustration"/>
    <circle cx="428" cy="776" r="40" fill="var(--orange)" stroke="var(--white)" stroke-width="6"/>
    <text x="428" y="776" class="stat stat-big fill-white">2</text>

    <rect x="0" y="829" width="330" height="30" class="fill-dark"/>
    <text x="6" y="853" class="label fill-white">Satisfied Customers</text>
    <circle cx="413" cy="860" r="36" fill="var(--white)" stroke="var(--dark)" stroke-width="6"/>
    <circle cx="413" cy="860" r="20" fill="var(--panel-right)" role="img" aria-label="Celebrating customer illustration"/>
    <circle cx="357" cy="847" r="40" fill="var(--white)" stroke="var(--dark)" stroke-width="8"/>
    <text x="357" y="847" class="stat stat-big fill-orange">54</text>
  </g>

  <g class="column-right">
    <path class="chain" stroke="var(--orange)" d="M686,172 L750,242"/>
    <path class="chain" stroke="var(--grey)" d="M750,242 L698,333"/>
    <path class="chain" stroke="var(--grey)" d="M698,333 L773,405"/>
    <path class="chain" stroke="var(--dark)" d="M773,405 L722,497"/>
    <path class="chain" stroke="var(--orange)" d="M722,497 L776,586"/>
    <path class="chain" stroke="var(--orange)" d="M776,586 L746,684"/>
    <path class="chain" stroke="var(--grey)" d="M746,684 L818,756"/>
    <path class="chain" stroke="var(--dark)" d="M818,756 L767,846"/>
    <path class="chain" stroke="var(--orange)" d="M767,846 L767,908"/>

    <rect x="720" y="150" width="430" height="30" class="fill-white"/>
    <text x="1120" y="174" class="label fill-orange right">QueryHub Pluten</text>
    <circle cx="618" cy="148" r="33" class="fill-white"/>
    <rect x="604" y="136" width="28" height="24" fill="var(--orange)" role="img" aria-label="Q&amp;A site icon"/>
    <circle cx="686" cy="172" r="40" fill="var(--orange)" stroke="var(--white)" stroke-width="6"/>
    <text x="686" y="172" class="stat stat-wide fill-white">24879</text>

    <rect x="760" y="228" width="390" height="30" class="fill-grey"/>
    <text x="1132" y="252" class="label fill-white right">Marketplace Downloads</text>
    <circle cx="685" cy="252" r="35" class="fill-grey"/>
    <path d="M670,252 L682,264 L702,238" stroke="var(--orange)" stroke-width="7" fill="none" stroke-linecap="round" stroke-linejoin="round"/>
    <circle cx="750" cy="242" r="38" fill="var(--white)" stroke="var(--grey)" stroke-width="8"/>
    <text x="750" y="242" class="stat stat-mid fill-grey">3601</text>

    <rect x="730" y="312" width="420" height="30" class="fill-white"/>
    <text x="1132" y="336" class="label fill-grey right">Total Chirper Followers</text>
    <circle cx="638" cy="322" r="30" class="fill-white"/>
    <circle cx="638" cy="322" r="16" fill="var(--grey)" role="img" aria-label="Social network icon"/>
    <circle cx="698" cy="333" r="38" fill="var(--grey)" stroke="var(--white)" stroke-width="6"/>
    <text x="698" y="333" class="stat stat-mid fill-white">7551</text>

    <rect x="800" y="390" width="350" height="30" class="fill-dark"/>
    <text x="814" y="414" class="label fill-white">X Attendees on X Meetups</text>
    <circle cx="706" cy="408" r="32" class="fill-dark"/>
    <g class="fill-white">
      <circle cx="692" cy="399" r="4"/><rect x="688" y="405" width="8" height="14"/>
      <circle cx="706" cy="399" r="4"/><rect x="702" y="405" width="8" height="14"/>
      <circle cx="720" cy="399" r="4"/><rect x="716" y="405" width="8" height="14"/>
    </g>
    <circle cx="773" cy="405" r="38" fill="var(--white)" stroke="var(--dark)" stroke-width="8"/>
    <text x="773" y="393" class="stat stat-wide fill-orange">433</text>
    <text x="773" y="416" class="stat stat-wide fill-orange">on 12</text>

    <rect x="755" y="478" width="395" height="30" class="fill-white"/>
    <text x="1132" y="502" class="label fill-orange right">Years of Experience</text>
    <circle cx="660" cy="508" r="32" class="fill-white"/>
    <path d="M648,492 L672,492 L660,508 L672,524 L648,524 L660,508 Z" class="fill-orange"/>
    <circle cx="722" cy="497" r="38" fill="var(--orange)" stroke="var(--white)" stroke-width="6"/>
    <text x="722" y="497" class="stat stat-mid fill-white">224</text>

    <rect x="810" y="567" width="340" height="30" class="fill-orange"/>
    <text x="1132" y="591" class="label fill-white right">Total Running Miles</text>
    <circle cx="710" cy="582" r="32" class="fill-orange"/>
    <circle cx="710" cy="582" r="16" fill="#f9a46e" role="img" aria-label="Runner figure"/>
    <circle cx="776" cy="586" r="40" fill="var(--white)" stroke="var(--orange)" stroke-width="8"/>
    <text x="776" y="572" class="stat stat-wide fill-orange">2384</text>
    <text x="776" y="600" class="stat stat-wide fill-orange">Kms</text>

    <rect x="780" y="665" width="370" height="30" class="fill-white"/>
    <text x="1132" y="689" class="label fill-grey right">New Cars</text>
    <circle cx="680" cy="695" r="35" class="fill-white"/>
    <rect x="656" y="688" width="48" height="16" rx="5" fill="var(--dark)" role="img" aria-label="Car illustration"/>
    <circle cx="746" cy="684" r="38" fill="var(--grey)" stroke="var(--white)" stroke-width="6"/>
    <text x="746" y="684" class="stat stat-big fill-white">5</text>

    <rect x="850" y="740" width="300" height="30" class="fill-white"/>
    <text x="1132" y="764" class="label fill-dark right">Musical Instruments</text>
    <text x="1132" y="793" class="label fill-dark right">Played by Team</text>
    <circle cx="760" cy="763" r="28" class="fill-white"/>
    <circle cx="760" cy="763" r="15" fill="var(--dark)" role="img" aria-label="Guitar and saxophone"/>
    <rect x="843" y="717" width="50" height="17" class="fill-white"/>
    <text x="846" y="730" class="tag fill-orange">Guitars</text>
    <rect x="856" y="774" width="38" height="17" class="fill-white"/>
    <text x="860" y="787" class="tag fill-orange">Sax</text>
    <circle cx="818" cy="756" r="38" fill="var(--dark)" stroke="var(--white)" stroke-width="6"/>
    <line x1="786" y1="756" x2="850" y2="756" stroke="var(--white)" stroke-width="1.5"/>
    <text x="818" y="740" class="stat stat-mid fill-white">43</text>
    <text x="818" y="773" class="stat stat-mid fill-white">1</text>

    <rect x="770" y="831" width="380" height="30" class="fill-orange"/>
    <text x="1132" y="855" class="label fill-white right">No. of Blue Screens</text>
    <text x="1132" y="886" class="label-sub fill-orange right">(Crashed Devices)</text>
    <circle cx="705" cy="830" r="40" class="fill-orange"/>
    <rect x="684" y="814" width="42" height="28" rx="2" fill="none" stroke="var(--white)" stroke-width="4"/>
    <rect x="676" y="845" width="58" height="5" rx="2" class="fill-white"/>
    <circle cx="767" cy="846" r="40" fill="var(--white)" stroke="var(--orange)" stroke-width="8"/>
    <text x="767" y="846" class="stat stat-big fill-orange">136</text>
  </g>

  <g class="footer">
    <rect x="0" y="908" width="1150" height="137" class="fill-white"/>
    <ellipse cx="575" cy="1058" rx="560" ry="22" fill="url(#floor-shadow)"/>
    <text x="18" y="986" class="sponsor fill-orange">DevSummit Platinum Sponsor</text>

    <circle cx="480" cy="975" r="26" class="fill-orange"/>
    <text x="521" y="988" class="brand-name fill-orange">Clovane</text>
    <text x="521" y="1021" class="brand-tagline fill-orange">Build smart. Move fast.</text>

    <polygon points="722,928 1150,928 1150,958 775,958" class="fill-dark"/>
    <text x="920" y="951" class="label fill-white">Memberships</text>

    <circle cx="768" cy="1016" r="17" fill="var(--partner-blue)"/>
    <text x="794" y="1025" class="partner" fill="var(--partner-blue)">Monoforge</text>
    <rect x="932" y="1002" width="28" height="28" fill="var(--partner-sky)"/>
    <text x="970" y="1025" class="partner" fill="var(--partner-sky)">Cloudspan</text>
  </g>
</svg>
</body>
</html>
```